BEACON CABS

Taxi card design

Need changes very slow in replying to my messages.

Target Market(s)

Customers

Industry/Entity Type

Taxi

Contact Information for Business Card

See previous design

Font styles to use
Sans Serif

Colors
A7469A
B969AE
D3A5CF
EDDBEB
F8F0F9
6B429C
8869AF
B7A5CE
E3DAEB
F3F0F8

Requirements
Nice to have
• We are in the business of looking after people, not just driving vehicles front
Should not have
• Front number 01632 480 480 needs to big big

```html
<!DOCTYPE html>
<html lang="en">
<head>
<meta charset="utf-8">
<title>Beacon Cabs – Business Card</title>
<link rel="stylesheet" href="https://fonts.googleapis.com/css2?family=Roboto:wght@400;700;900&display=swap">
<style>
  :root{
    --stage:#2b2b2d;
    --purple:#9561c4;
    --purple-deep:#6f2fb0;
    --purple-dark:#33197a;
    --panel:#ebebeb;
    --ink:#1e1e20;
    --black:#1b1c1e;
    --white:#ffffff;
  }
  *{box-sizing:border-box;margin:0;padding:0}
  html,body{width:1200px;height:900px;overflow:hidden}
  body{background:var(--stage);font-family:"Roboto",Arial,sans-serif;display:flex;align-items:center;justify-content:center;gap:30px}
  .card{position:relative;width:560px;height:320px;border-radius:14px;overflow:hidden}

  /* front */
  .card--front{background:var(--panel)}
  .front__wedge{position:absolute;inset:0;width:100%;height:100%}
  .front__services{position:absolute;top:0;left:0;right:0;height:46px;background:var(--purple);display:flex;align-items:center;justify-content:center;gap:22px;font-size:13px;letter-spacing:.5px;color:var(--ink);text-transform:uppercase}
  .brand{position:absolute;top:64px;left:150px;font-weight:900;font-size:44px;letter-spacing:-1px;color:var(--ink);line-height:1}
  .brand__tag{position:absolute;top:116px;left:330px;font-size:19px;color:var(--ink)}
  .front__main{position:absolute;top:140px;left:70px;display:flex;align-items:center;gap:10px;font-weight:900;font-size:42px;color:var(--ink);letter-spacing:-.5px}
  .front__main svg{width:30px;height:30px;fill:var(--ink)}
  .front__details{position:absolute;top:196px;left:108px;font-size:13.5px;color:var(--ink);line-height:1.35}
  .front__lines{position:absolute;left:0;right:0;bottom:0;height:44px;display:flex;gap:8px}
  .line-tab{flex:1;background:var(--purple-dark);border-radius:0 14px 0 0;display:flex;align-items:center;justify-content:center;gap:6px;color:var(--white);font-weight:700;font-size:15px}
  .line-tab svg{width:14px;height:14px;fill:var(--white)}

  /* back */
  .card--back{background:var(--black)}
  .back__rule{position:absolute;left:0;right:0;top:168px;height:4px;background:var(--white)}
  .back__brand{position:absolute;top:140px;left:50%;transform:translateX(-50%);background:var(--black);padding:0 22px;font-weight:900;font-size:48px;letter-spacing:-1px;color:var(--white);line-height:1.2;white-space:nowrap}
  .back__phone{position:absolute;top:38px;left:110px;display:flex;align-items:center;gap:14px;color:var(--white);font-weight:900;font-size:44px}
  .back__phone-icon{width:44px;height:44px;border-radius:9px;background:var(--white);display:flex;align-items:center;justify-content:center}
  .back__phone-icon svg{width:26px;height:26px;fill:var(--black)}
  .back__address{position:absolute;left:0;right:0;bottom:30px;text-align:center;color:var(--white);font-weight:700;font-size:17px}
</style>
</head>
<body>

<section class="card card--front" aria-label="Card front">
  <svg class="front__wedge" viewBox="0 0 560 320" preserveAspectRatio="none" aria-hidden="true">
    <polygon points="0,46 175,46 430,320 0,320" fill="var(--purple)"/>
  </svg>
  <div class="front__services">
    <span>Airport Transfers</span><span>|</span><span>Minibuses</span><span>|</span><span>School Transport</span>
  </div>
  <div class="brand">BEACON CABS</div>
  <div class="brand__tag">24/7 Service</div>
  <div class="front__main">
    <svg viewBox="0 0 24 24" aria-hidden="true"><path d="M6.6 10.8a15.1 15.1 0 0 0 6.6 6.6l2.2-2.2a1 1 0 0 1 1-.25 11.4 11.4 0 0 0 3.6.57 1 1 0 0 1 1 1V20a1 1 0 0 1-1 1A17 17 0 0 1 3 4a1 1 0 0 1 1-1h3.5a1 1 0 0 1 1 1c0 1.25.2 2.45.57 3.57a1 1 0 0 1-.25 1z"/></svg>
    <span>01632 480 480</span>
  </div>
  <div class="front__details">
    <p>Freephone: 0808 157 0 000</p>
    <p>Email: bookings@beaconcabs.example</p>
    <p>Website: www.beaconcabs.example</p>
  </div>
  <div class="front__lines">
    <div class="line-tab"><svg viewBox="0 0 24 24" aria-hidden="true"><path d="M6.6 10.8a15.1 15.1 0 0 0 6.6 6.6l2.2-2.2a1 1 0 0 1 1-.25 11.4 11.4 0 0 0 3.6.57 1 1 0 0 1 1 1V20a1 1 0 0 1-1 1A17 17 0 0 1 3 4a1 1 0 0 1 1-1h3.5a1 1 0 0 1 1 1c0 1.25.2 2.45.57 3.57a1 1 0 0 1-.25 1z"/></svg>01632 96 01 11</div>
    <div class="line-tab"><svg viewBox="0 0 24 24" aria-hidden="true"><path d="M6.6 10.8a15.1 15.1 0 0 0 6.6 6.6l2.2-2.2a1 1 0 0 1 1-.25 11.4 11.4 0 0 0 3.6.57 1 1 0 0 1 1 1V20a1 1 0 0 1-1 1A17 17 0 0 1 3 4a1 1 0 0 1 1-1h3.5a1 1 0 0 1 1 1c0 1.25.2 2.45.57 3.57a1 1 0 0 1-.25 1z"/></svg>01632 96 02 22</div>
    <div class="line-tab"><svg viewBox="0 0 24 24" aria-hidden="true"><path d="M6.6 10.8a15.1 15.1 0 0 0 6.6 6.6l2.2-2.2a1 1 0 0 1 1-.25 11.4 11.4 0 0 0 3.6.57 1 1 0 0 1 1 1V20a1 1 0 0 1-1 1A17 17 0 0 1 3 4a1 1 0 0 1 1-1h3.5a1 1 0 0 1 1 1c0 1.25.2 2.45.57 3.57a1 1 0 0 1-.25 1z"/></svg>01632 96 0333</div>
  </div>
</section>

<section class="card card--back" aria-label="Card back">
  <div class="back__phone">
    <span class="back__phone-icon"><svg viewBox="0 0 24 24" aria-hidden="true"><path d="M6.6 10.8a15.1 15.1 0 0 0 6.6 6.6l2.2-2.2a1 1 0 0 1 1-.25 11.4 11.4 0 0 0 3.6.57 1 1 0 0 1 1 1V20a1 1 0 0 1-1 1A17 17 0 0 1 3 4a1 1 0 0 1 1-1h3.5a1 1 0 0 1 1 1c0 1.25.2 2.45.57 3.57a1 1 0 0 1-.25 1z"/></svg></span>
    <span>01632 480 480</span>
  </div>
  <div class="back__rule"></div>
  <div class="back__brand">BEACON CABS</div>
  <p class="back__address">Harbour Lane Depot, Mill Row, Northbridge, NB4 7QT</p>
</section>

</body>
</html>
```